Web Design Project - vR Advise

We want to modernise our web page profile. We have an existing web site that we are particularly not proud of (www.vradvise.com.au).
We have started to build a new web site using Joomla and we like the structure of it, but we need it to be professionally designed and implemented.

This current development site can be viewed here: dev.vradvise.com.au

We would like a complete design for the entire website, ready for deployment.

(We still need to finalise the content, as we have just developed new products that we hope to launch in August both on this web site and by a Vendor Forum.)
Updates

Target Market(s)

Larger companies where the robustness of their IT infrastructure is critical. Our tools and services provide for monitoring of every device

Industry/Entity Type

Build

Requirements
Must have
• Responsive design for different screen sizes.

BrightDock help desk software integrated with the website.
Currently can be viewed at support.vradvise.com.au
Brightdock only supports custom css.

Nice to have
• Customer experience testimonials in a rotating banner
Chirpr and Pagebook links in the footer
We use Avenir as a company font.
Use company colours as in the logo (green and blue)

```html
<!DOCTYPE html>
<html lang="en">
<head>
<meta charset="utf-8">
<title>vR Advise – Any Device, Any Platform, Anywhere</title>
<link rel="stylesheet" href="https://fonts.googleapis.com/css2?family=Open+Sans:wght@400;600;700&family=PT+Sans+Narrow:wght@700&display=swap">
<style>
  :root{
    --green:#6bb82c;
    --blue:#1f9fd8;
    --teal:#2aa3b8;
    --teal-dark:#1d8a9e;
    --teal-deep:#17606f;
    --ink:#3a3a3a;
    --muted:#8a8a8a;
    --nav:#6f6f6f;
    --white:#ffffff;
    --hero-a:#3b2c22;
    --hero-b:#5e4a3c;
    --hero-c:#45403e;
  }
  *{box-sizing:border-box;margin:0;padding:0}
  html,body{width:1200px;height:943px;overflow:hidden;background:#fff}
  body{font-family:"Open Sans",Arial,sans-serif;color:var(--ink)}
  .page{width:1200px;height:943px;position:relative;overflow:hidden}

  .site-header{height:72px;display:flex;align-items:center;justify-content:space-between;padding:0 190px 0 160px;background:var(--white)}
  .brand{display:flex;align-items:center;gap:8px;font-weight:700;font-size:22px;color:var(--blue)}
  .brand-dot{width:14px;height:14px;border-radius:50%;background:var(--green)}
  .main-nav{display:flex;gap:26px}
  .main-nav a{font-size:12px;font-weight:700;color:var(--nav);text-decoration:none;letter-spacing:.3px}

  .hero{height:372px;position:relative;overflow:hidden}
  .hero-photo{position:absolute;inset:0;
    background:linear-gradient(100deg,var(--hero-a) 0%,var(--hero-b) 50%,var(--hero-c) 100%)}
  .hero-copy{position:absolute;left:158px;top:76px;color:var(--white)}
  .hero-title{font-family:"PT Sans Narrow","Arial Narrow",sans-serif;font-weight:700;font-size:38px;line-height:1.05;text-transform:uppercase}
  .hero-text{margin-top:22px;font-size:14px;line-height:1.35;width:290px}
  .btn-primary{display:inline-block;margin-top:28px;width:210px;height:44px;line-height:44px;text-align:center;
    background:var(--green);color:var(--white);font-weight:600;font-size:16px;border-radius:3px;
    box-shadow:0 0 0 4px rgba(0,0,0,.25)}
  .slider-arrow{position:absolute;top:165px;width:48px;height:48px;border-radius:50%;background:rgba(60,60,60,.55);
    display:flex;align-items:center;justify-content:center}
  .slider-arrow.prev{left:40px}
  .slider-arrow.next{right:40px}

  .services{height:230px;text-align:center;padding-top:30px}
  .section-title{font-size:24px;font-weight:400;letter-spacing:.5px;color:#555}
  .section-title .accent{font-weight:700}
  .services .section-title .accent{color:var(--teal)}
  .service-list{display:flex;justify-content:center;gap:70px;margin-top:20px}
  .service{width:240px}
  .hex{width:58px;height:64px;margin:0 auto;display:block}
  .service-name{margin-top:8px;font-size:12px;color:#555}
  .service-name span{color:var(--blue)}
  .service-desc{margin-top:5px;font-size:9.5px;line-height:1.4;color:var(--muted)}

  .products{height:269px;background:linear-gradient(180deg,var(--teal) 0%,var(--teal-dark) 100%);padding-top:20px;text-align:center}
  .products .section-title{color:var(--white)}
  .products .section-title .accent{color:#0d4d60}
  .product-grid{display:grid;grid-template-columns:330px 330px;column-gap:110px;row-gap:14px;justify-content:center;margin-top:16px;text-align:left}
  .product{display:flex;gap:14px}
  .product-hex{width:48px;height:54px;flex:none}
  .product-title{font-size:12px;font-weight:600;color:var(--white)}
  .product-desc{margin-top:3px;font-size:9.5px;line-height:1.4;color:#d9f1f5}
  .btn-small{display:inline-block;margin-top:5px;padding:2px 10px;font-size:9px;background:#35d0e0;color:#0d4d60;border-radius:2px}
</style>
</head>
<body>
<div class="page">
  <header class="site-header">
    <div class="brand"><span class="brand-dot"></span>vR Advise</div>
    <nav class="main-nav">
      <a href="#">HOME</a><a href="#">SERVICES</a><a href="#">PRODUCTS</a><a href="#">SUPPORT</a><a href="#">ABOUT US</a><a href="#">CONTACT</a>
    </nav>
  </header>

  <section class="hero">
    <div class="hero-photo" role="img" aria-label="Hero photograph: blurred office background with a hand holding a smartphone"></div>
    <div class="hero-copy">
      <h1 class="hero-title">Any device, any<br>platorm, anywhere</h1>
      <p class="hero-text">Cross-Domain, performance and services and level monitoring and management.</p>
      <a class="btn-primary">Learn More</a>
    </div>
    <div class="slider-arrow prev"><svg width="14" height="18" viewBox="0 0 14 18"><path d="M10 2 L3 9 L10 16" stroke="#fff" stroke-width="3" fill="none"/></svg></div>
    <div class="slider-arrow next"><svg width="14" height="18" viewBox="0 0 14 18"><path d="M4 2 L11 9 L4 16" stroke="#fff" stroke-width="3" fill="none"/></svg></div>
  </section>

  <section class="services">
    <h2 class="section-title"><span class="accent">vR Advise</span> SERVICES</h2>
    <div class="service-list">
      <div class="service">
        <svg class="hex" viewBox="0 0 58 64"><polygon points="29,0 58,16 58,48 29,64 0,48 0,16" fill="var(--green)"/><text x="29" y="41" text-anchor="middle" font-size="26" fill="#fff" font-family="Arial,sans-serif">⌘</text></svg>
        <p class="service-name">Consulting <span>SERVICES</span></p>
        <p class="service-desc">Leveraging architecture and consulting skills to deliver a technology approach and ideas, supported by vR Advise professional and operational support.</p>
      </div>
      <div class="service">
        <svg class="hex" viewBox="0 0 58 64"><polygon points="29,0 58,16 58,48 29,64 0,48 0,16" fill="var(--green)"/><circle cx="29" cy="25" r="6" fill="#fff"/><path d="M18 44 Q29 28 40 44 Z" fill="#fff"/></svg>
        <p class="service-name">Professional <span>SERVICES</span></p>
        <p class="service-desc">Leveraging architecture and consulting skills to deliver a technology approach and ideas, supported by vR Advise professional and operational support.</p>
      </div>
      <div class="service">
        <svg class="hex" viewBox="0 0 58 64"><polygon points="29,0 58,16 58,48 29,64 0,48 0,16" fill="var(--green)"/><polygon points="29,19 41,25 41,39 29,45 17,39 17,25" fill="#fff"/><path d="M17 25 L29 31 L41 25 M29 31 V45" stroke="var(--green)" stroke-width="2" fill="none"/></svg>
        <p class="service-name">Productised <span>SERVICES</span></p>
        <p class="service-desc">Leveraging architecture and consulting skills to deliver a technology approach and ideas, supported by vR Advise professional and operational support.</p>
      </div>
    </div>
  </section>

  <section class="products">
    <h2 class="section-title"><span class="accent">vR Advise</span> PRODUCTS</h2>
    <div class="product-grid">
      <div class="product">
        <svg class="product-hex" viewBox="0 0 48 54"><polygon points="24,0 48,13 48,41 24,54 0,41 0,13" fill="var(--teal-deep)"/><text x="24" y="32" text-anchor="middle" font-size="13" fill="#fff" font-family="Open Sans,sans-serif">vR</text></svg>
        <div><p class="product-title">vR Advise Products</p><p class="product-desc">vR Advise developed products, complementary solutions to our vendor products, from phone applications to cross-platform integrations for our partner range.</p><span class="btn-small">Learn More</span></div>
      </div>
      <div class="product">
        <svg class="product-hex" viewBox="0 0 48 54"><polygon points="24,0 48,13 48,41 24,54 0,41 0,13" fill="var(--teal-deep)"/><text x="24" y="32" text-anchor="middle" font-size="13" fill="#fff" font-family="Open Sans,sans-serif">vR</text></svg>
        <div><p class="product-title">vR Advise Products</p><p class="product-desc">vR Advise developed products, complementary solutions to our vendor products, from phone applications to cross-platform integrations for our partner range.</p><span class="btn-small">Learn More</span></div>
      </div>
      <div class="product">
        <svg class="product-hex" viewBox="0 0 48 54"><polygon points="24,0 48,13 48,41 24,54 0,41 0,13" fill="var(--teal-deep)"/><text x="24" y="32" text-anchor="middle" font-size="13" fill="#fff" font-family="Open Sans,sans-serif">vR</text></svg>
        <div><p class="product-title">vR Advise Products</p><p class="product-desc">vR Advise developed products, complementary solutions to our vendor products, from phone applications to cross-platform integrations for our partner range.</p><span class="btn-small">Learn More</span></div>
      </div>
      <div class="product">
        <svg class="product-hex" viewBox="0 0 48 54"><polygon points="24,0 48,13 48,41 24,54 0,41 0,13" fill="var(--teal-deep)"/><text x="24" y="32" text-anchor="middle" font-size="13" fill="#fff" font-family="Open Sans,sans-serif">vR</text></svg>
        <div><p class="product-title">vR Advise Products</p><p class="product-desc">vR Advise developed products, complementary solutions to our vendor products, from phone applications to cross-platform integrations for our partner range.</p><span class="btn-small">Learn More</span></div>
      </div>
    </div>
  </section>
</div>
</body>
</html>
```